Web Design for an Innovative Life Science Marketplace

IMPORTANT:
The software is called CS-Cart. It has capabilities and limitations with design features in the software. There is a certain framework that needs to be followed. It is PHP and Linux. It may require add-ons for your design, so please be specific with what is required. It’s preferred the designer has CS-Cart knowledge/experience.

Key Requirements
1. I’d like the design to include an implemented/recommended CS-Cart theme that is consistent with our branding (see the marketing collateral and logo).
2. I then need the additional design changes to that theme to create the below web pages.
3. All designs should be consistent with our branding. All pictures should either be computer generated (clip art-like) or pictures of happy patients. What is a happy patient? Close up photo of someone healthy, happy, and experiencing/enjoying life. Not someone in a hospital or getting care. Please see examples already on the site.

Please see the attached Web Design details in the word document. That document is important to complete the design.

```html
<!DOCTYPE html>
<html lang="en">
<head>
<meta charset="utf-8">
<title>LoopSource – Circular Supply Chain Marketplace</title>
<link rel="stylesheet" href="https://fonts.googleapis.com/css2?family=Montserrat:wght@400;600;700;800&family=Open+Sans:wght@400;600;700&display=swap">
<style>
:root{
  --teal:#1b8a78;
  --teal-dark:#146b5e;
  --green:#8cc63f;
  --green-dark:#6fa82a;
  --ink:#333a3a;
  --muted:#777;
  --line:#e3e3e3;
  --light:#f5f6f5;
  --white:#fff;
}
*{box-sizing:border-box;margin:0;padding:0}
html,body{width:1200px;height:2824px;overflow:hidden}
body{font-family:"Open Sans",Arial,sans-serif;color:var(--ink);background:var(--white);position:relative}
h1,h2,h3,h4,.brand,.btn,.nav a{font-family:"Montserrat",Arial,sans-serif}

/* header */
.topbar{height:88px;display:flex;align-items:center;padding:0 80px;gap:40px}
.brand{display:flex;align-items:center;gap:10px;font-weight:800;font-size:26px;color:var(--teal)}
.brand-dot{width:34px;height:34px;border-radius:50%;background:var(--green)}
.search{margin-left:160px;display:flex;width:480px;height:36px}
.search-field{flex:1;border:1px solid var(--line);border-right:0;padding:0 14px;font-size:13px;color:#aaa;display:flex;align-items:center}
.search-btn{width:110px;background:var(--green);color:#fff;font-weight:700;font-size:13px;display:flex;align-items:center;justify-content:center;font-family:"Montserrat",sans-serif}
.account{margin-left:auto;font-size:13px;color:var(--muted)}
.nav{height:40px;display:flex;align-items:center;gap:34px;padding:0 80px;border-top:1px solid var(--line)}
.nav a{font-size:12px;font-weight:600;color:var(--ink);text-decoration:none;letter-spacing:.5px}

/* hero */
.hero{position:relative;height:424px}
.hero-photo{position:absolute;inset:0;background:linear-gradient(120deg,#cfe3d6 0%,#a8c4b4 40%,#7d9f8c 70%,#c9d8cf 100%)}
.hero-panel{position:absolute;right:0;top:0;width:620px;height:424px;background:linear-gradient(90deg,rgba(27,138,120,.85),rgba(27,138,120,.95));clip-path:polygon(12% 0,100% 0,100% 100%,0 100%);padding:90px 80px 0 150px;color:#fff}
.hero-panel h1{font-size:40px;font-weight:800;line-height:1.1;margin-bottom:24px}
.hero-panel p{font-size:14px;line-height:1.6;margin-bottom:28px}
.btn{display:inline-block;background:var(--green);color:#fff;font-weight:700;font-size:12px;letter-spacing:.6px;padding:11px 24px}

/* section heads */
.section-head{text-align:center}
.section-head h2{font-size:32px;font-weight:800;letter-spacing:1px}
.divider{display:flex;align-items:center;justify-content:center;gap:10px;margin:14px 0 12px}
.divider span{width:60px;height:2px;background:var(--green)}
.divider i{width:14px;height:14px;border-radius:50%;border:2px solid var(--green)}
.section-head p{font-size:13px;color:var(--muted)}

/* who should join */
.join{height:460px;padding-top:190px}
.join-cards{display:flex;gap:24px;justify-content:center;margin-top:40px}
.join-card{width:300px;height:130px;padding:18px 22px;color:#fff}
.join-card h3{font-size:17px;font-weight:800;margin-bottom:12px}
.join-card p{font-size:12px;line-height:1.5}
.c-teal{background:var(--teal)}
.c-white{background:#fff;color:var(--ink);border:1px solid var(--line);box-shadow:0 4px 14px rgba(0,0,0,.08)}
.c-white h3{color:var(--teal)}
.c-green{background:var(--green)}

/* products */
.products{position:relative;height:528px;color:#fff}
.products-bg{position:absolute;inset:0;background:linear-gradient(135deg,#3a3230,#5b2b24 35%,#2e3a36 70%,#3d3532)}
.products-inner{position:relative;padding-top:60px}
.products .section-head p{color:#ddd}
.product-cards{display:flex;gap:24px;justify-content:center;margin-top:50px}
.product-card{width:220px;height:220px;background:rgba(255,255,255,.94);color:var(--ink);text-align:center;padding:24px 20px}
.icon-ring{width:64px;height:64px;border-radius:50%;border:2px solid var(--green);margin:0 auto 14px;display:flex;align-items:center;justify-content:center}
.product-card h3{font-size:15px;font-weight:800;color:var(--teal);margin-bottom:8px;line-height:1.2}
.product-card p{font-size:11px;line-height:1.5;color:var(--muted)}

/* marketing */
.marketing{height:580px;padding-top:100px}
.materials{position:relative;width:1040px;height:300px;margin:46px auto 0}
.mat{position:absolute;top:0;height:300px;padding:40px 50px;color:#fff}
.mat-left{left:0;width:600px;background:var(--teal);clip-path:polygon(0 0,100% 0,88% 100%,0 100%)}
.mat-right{right:0;width:540px;background:var(--green);clip-path:polygon(13% 0,100% 0,100% 100%,0 100%);padding-left:110px}
.mat h3{font-size:20px;font-weight:800;margin-bottom:14px}
.mat p{font-size:12px;line-height:1.6;width:380px;margin-bottom:22px}
.mat .btn{background:rgba(0,0,0,.18)}
.mat-left .btn{background:var(--green)}
.mat-right .btn{background:var(--teal)}

/* promise */
.promise{position:relative;height:320px;margin-top:40px;color:#fff;text-align:center}
.promise-bg{position:absolute;inset:0;background:linear-gradient(90deg,#5f6a6c,#8e9a9c 50%,#5c6669)}
.promise-inner{position:relative;padding-top:100px}
.promise h2{font-size:32px;font-weight:800;letter-spacing:1px}
.promise .divider span{background:#fff}
.promise .divider i{border-color:#fff}
.promise blockquote{font-size:22px;font-weight:600;line-height:1.4;width:720px;margin:0 auto}

/* footer */
.footer{display:flex;padding:60px 80px 0;gap:60px}
.footer h4{font-size:15px;font-weight:800;margin-bottom:16px}
.footer li{list-style:none;font-size:12px;color:var(--muted);line-height:1.9}
.f-about{width:260px}
.f-about p{font-size:12px;color:var(--muted);line-height:1.6;margin:16px 0 20px}
.f-col{width:180px}
.socials{display:flex;gap:10px;margin-top:16px}
.socials i{width:26px;height:26px;border-radius:50%;border:1.5px solid var(--green)}
.contact li{display:flex;gap:10px;align-items:flex-start;margin-bottom:8px;line-height:1.5}
.contact svg{flex:none;margin-top:2px}
</style>
</head>
<body>

<header class="topbar">
  <div class="brand"><span class="brand-dot"></span>LoopSource</div>
  <div class="search"><div class="search-field">Search...</div><div class="search-btn">SEARCH</div></div>
  <div class="account">My Account ▾</div>
</header>
<nav class="nav">
  <a>HOME</a><a>WHY LOOPSOURCE</a><a>ABOUT US</a><a>OUR PARTNERS</a><a>WHITE PAPER</a><a>QUALITY POLICY</a>
</nav>

<section class="hero">
  <div class="hero-photo" role="img" aria-label="Photo of a smiling man jogging outdoors on a sunny street"></div>
  <div class="hero-panel">
    <h1>JOIN THE CIRCULAR<br>SUPPLY CHAIN</h1>
    <p>A virtual multi-vendor marketplace and hub for the life sciences community to connect and trade certified surplus and after-market materials and equipment.</p>
    <span class="btn">PRE REGISTER</span>
  </div>
</section>

<section class="join">
  <div class="section-head">
    <h2>WHO SHOULD JOIN</h2>
    <div class="divider"><span></span><i></i><span></span></div>
    <p>Lorem Ipsum is simply dummy text of the printing and typesetting industry.</p>
  </div>
  <div class="join-cards">
    <div class="join-card c-teal"><h3>MANUFACTURERS</h3><p>Create an account in minutes to list surplus stock or source certified materials and equipment.</p></div>
    <div class="join-card c-white"><h3>RESEARCHERS</h3><p>Stretch your lab budget with verified materials and quality reviewed equipment.</p></div>
    <div class="join-card c-green"><h3>ORIGINAL SUPPLIERS</h3><p>Reach new buyers and give unused products a second life in research.</p></div>
  </div>
</section>

<section class="products">
  <div class="products-bg" role="img" aria-label="Photo of a laboratory workbench with colourful equipment, darkened"></div>
  <div class="products-inner">
    <div class="section-head">
      <h2>PRODUCTS</h2>
      <div class="divider"><span></span><i></i><span></span></div>
      <p>Lorem Ipsum is simply dummy text of the printing and typesetting industry.</p>
    </div>
    <div class="product-cards">
      <div class="product-card">
        <div class="icon-ring"><svg width="30" height="30" viewBox="0 0 30 30" fill="none" stroke="#1b8a78" stroke-width="2"><path d="M11 3h8M12 3v9L5 26h20L18 12V3"/></svg></div>
        <h3>RAW MATERIALS</h3><p>Surplus and expiring materials at fair prices for labs.</p>
      </div>
      <div class="product-card">
        <div class="icon-ring"><svg width="30" height="30" viewBox="0 0 30 30" fill="none" stroke="#1b8a78" stroke-width="2"><rect x="5" y="8" width="20" height="16"/><path d="M10 8V5h10v3M9 16h12"/></svg></div>
        <h3>EQUIPMENT</h3><p>Certified pre-owned instruments ready for new applications.</p>
      </div>
      <div class="product-card">
        <div class="icon-ring"><svg width="30" height="30" viewBox="0 0 30 30" fill="none" stroke="#1b8a78" stroke-width="2"><circle cx="15" cy="15" r="5"/><path d="M15 4v4M15 22v4M4 15h4M22 15h4"/></svg></div>
        <h3>PARTS</h3><p>Components and spares for key instrument systems.</p>
      </div>
      <div class="product-card">
        <div class="icon-ring"><svg width="30" height="30" viewBox="0 0 30 30" fill="none" stroke="#1b8a78" stroke-width="2"><circle cx="10" cy="11" r="4"/><circle cx="20" cy="11" r="4"/><path d="M3 25c1-5 4-7 7-7s6 2 7 7M13 25c1-5 4-7 7-7s6 2 7 7"/></svg></div>
        <h3>COLLABORATIVE RELATIONSHIPS</h3><p>Build lasting partners across the supply chain.</p>
      </div>
    </div>
  </div>
</section>

<section class="marketing">
  <div class="section-head">
    <h2>MARKETING MATERIALS</h2>
    <div class="divider"><span></span><i></i><span></span></div>
    <p>Lorem Ipsum is simply dummy text of the printing and typesetting industry.</p>
  </div>
  <div class="materials">
    <div class="mat mat-left">
      <h3>READ OUR WHITE PAPER</h3>
      <p>It is a long established fact that a reader will be distracted by the readable content of a page when looking at its layout and structure.</p>
      <span class="btn">DOWNLOAD WHITE PAPER</span>
    </div>
    <div class="mat mat-right">
      <h3>READ OUR BROCHURE</h3>
      <p>It is a long established fact that a reader will be distracted by the readable content of a page when looking at its layout.</p>
      <span class="btn">DOWNLOAD BROCHURE</span>
    </div>
  </div>
</section>

<section class="promise">
  <div class="promise-bg" role="img" aria-label="Photo of two people shaking hands"></div>
  <div class="promise-inner">
    <h2>PROMISE</h2>
    <div class="divider"><span></span><i></i><span></span></div>
    <blockquote>“A greener, more cost-efficient, and quality-driven supply chain through a collaborative life sciences marketplace”</blockquote>
  </div>
</section>

<footer class="footer">
  <div class="f-about">
    <div class="brand"><span class="brand-dot"></span>LoopSource</div>
    <p>It is a long established fact that a reader will be distracted by the readable content.</p>
    <p>Copyright 2024 | All Rights Reserved</p>
  </div>
  <div class="f-col">
    <h4>QUICK LINKS</h4>
    <ul><li>Home</li><li>Why LoopSource</li><li>About Us</li><li>Our Partners</li><li>White Paper</li><li>Quality Policy</li></ul>
  </div>
  <div class="f-col">
    <h4>MY ACCOUNT</h4>
    <ul><li>Login</li><li>Register</li><li>Privacy Policy</li></ul>
    <div class="socials"><i></i><i></i><i></i></div>
  </div>
  <div class="f-col contact" style="width:260px">
    <h4>CONTACT INFO</h4>
    <ul>
      <li><svg width="14" height="14" viewBox="0 0 14 14" fill="none" stroke="#8cc63f" stroke-width="1.5"><path d="M7 13s5-5 5-8A5 5 0 0 0 2 5c0 3 5 8 5 8z"/><circle cx="7" cy="5" r="1.6"/></svg>214 Meridian Way, Suite 3<br>Harbor City, ST 00000</li>
      <li><svg width="14" height="14" viewBox="0 0 14 14" fill="none" stroke="#8cc63f" stroke-width="1.5"><path d="M3 1h3l1 3-2 1a7 7 0 0 0 4 4l1-2 3 1v3a1 1 0 0 1-1 1A11 11 0 0 1 2 2a1 1 0 0 1 1-1z"/></svg>+1 555 014 7720</li>
      <li><svg width="14" height="14" viewBox="0 0 14 14" fill="none" stroke="#8cc63f" stroke-width="1.5"><rect x="1" y="3" width="12" height="8"/><path d="M1 3l6 5 6-5"/></svg>hello@loopsource.example</li>
    </ul>
  </div>
</footer>

</body>
</html>
```